Vell Partners Building Business Cards

We need a business card that reflects our business as "Solar Experts" in San Diego. Browse our website www.vellpartners.example our License needs to be displayed as "CSLB# 4718392" our phone number is (619) 555-0147

Save thousands on your electric bills and increase the value of your home while helping to protect the environment. Our solar installation experts will help you design the system that's right for you, using only the highest quality equipment that will look great and give you ideal performance. Our goal is to make you energy independent, and get your electric bill to 0.

Tobias Wrenfield
(619) 555-0147
tobias@vellpartners.example

Target Market(s)

Home owners in san diego looking for solar

Industry/Entity Type

Solar Energy

Contact Information for Business Card

Tobias Wrenfield
(619) 555-0147
tobias@vellpartners.example

Font styles to use
Other font styles liked:
• Use our logo font

Requirements
Must have
• License needs to be displayed as "CSLB# 4718392" our phone number is (619) 555-0147
Nice to have
• Real images of rooftop home solar in san diego
Should not have
• our business address

```html
<!DOCTYPE html>
<html lang="en">
<head>
<meta charset="utf-8">
<title>Vell Partners Building – Business Cards</title>
<link rel="stylesheet" href="https://fonts.googleapis.com/css2?family=Cinzel:wght@400;600&family=Roboto:wght@400;700&family=Tinos:ital@1&display=swap">
<style>
  :root {
    --backdrop: #e9e6e2;
    --navy: #1f3c78;
    --navy-ink: #1a3a73;
    --sun: #f5a81c;
    --white: #ffffff;
    --grey-text: #5f6166;
    --card-shadow: 0 6px 14px rgba(0, 0, 0, 0.25);
  }
  * { box-sizing: border-box; margin: 0; padding: 0; }
  html, body {
    width: 1200px;
    height: 1000px;
    overflow: hidden;
    background: var(--backdrop);
  }
  .canvas {
    position: relative;
    width: 1200px;
    height: 1000px;
  }
  .card {
    position: absolute;
    left: 220px;
    width: 760px;
    box-shadow: var(--card-shadow);
  }
  .card--front {
    top: 50px;
    height: 433px;
    background: var(--navy);
  }
  .card--back {
    top: 524px;
    height: 436px;
    background: var(--white);
  }
  .brand {
    position: absolute;
    left: 0;
    right: 0;
    display: flex;
    justify-content: center;
    align-items: center;
    gap: 16px;
  }
  .brand__dot {
    width: 30px;
    height: 30px;
    border-radius: 50%;
    background: var(--sun);
    flex: none;
  }
  .brand__name {
    font-family: "Roboto", Arial, sans-serif;
    font-weight: 700;
    font-size: 50px;
    letter-spacing: -1px;
    line-height: 1;
  }
  .card--front .brand { top: 195px; }
  .card--front .brand__name { color: var(--white); }
  .card--back .brand { top: 130px; }
  .card--back .brand__name { color: var(--navy-ink); }
  .tagline {
    position: absolute;
    top: 352px;
    left: 0;
    right: 0;
    text-align: center;
    font-family: "Tinos", "Times New Roman", serif;
    font-style: italic;
    font-size: 27px;
    color: var(--white);
    letter-spacing: 0.5px;
  }
  .holder {
    position: absolute;
    top: 254px;
    left: 0;
    right: 0;
    text-align: center;
    font-family: "Cinzel", "Times New Roman", serif;
    font-weight: 600;
    font-size: 22px;
    letter-spacing: 1.5px;
    color: var(--navy-ink);
  }
  .holder__rule {
    position: absolute;
    top: 287px;
    left: 280px;
    width: 200px;
    height: 2px;
    background: linear-gradient(to right, rgba(26,58,115,0), var(--navy-ink) 50%, rgba(26,58,115,0));
  }
  .contact {
    position: absolute;
    top: 302px;
    left: 0;
    right: 0;
    text-align: center;
    font-family: "Roboto", Arial, sans-serif;
    font-size: 17.5px;
    color: var(--grey-text);
    letter-spacing: 0.2px;
  }
  .contact__sep {
    color: var(--sun);
    margin: 0 10px;
  }
  .license {
    position: absolute;
    top: 340px;
    left: 0;
    right: 0;
    text-align: center;
    font-family: "Roboto", Arial, sans-serif;
    font-size: 15px;
    color: var(--grey-text);
    letter-spacing: 0.6px;
  }
</style>
</head>
<body>
<main class="canvas">
  <section class="card card--front" aria-label="Card front">
    <div class="brand">
      <span class="brand__name">Vell Partners Building</span>
      <span class="brand__dot"></span>
    </div>
    <p class="tagline">The Solar Experts</p>
  </section>

  <section class="card card--back" aria-label="Card back">
    <div class="brand">
      <span class="brand__name">Vell Partners Building</span>
      <span class="brand__dot"></span>
    </div>
    <p class="holder">Tobias Wrenfield</p>
    <div class="holder__rule"></div>
    <p class="contact">(619) 555-0147<span class="contact__sep">|</span>tobias@vellpartners.example<span class="contact__sep">|</span>www.vellpartners.example</p>
    <p class="license">CSLB# 4718392</p>
  </section>
</main>
</body>
</html>
```